Website for software company "velmor"

We need a website for our software company/startup named "velmor". We are developing several products (currently 3 standard-software products) which are all in different sectors, but all our products are available for Laptops/PC/Mobile Phones/Tablets, ... We do also create custom software and support our customers with consulting to optimize their processes.
We already have a Logo which you can find in the attached files.
We are a young team of 4 members (two founders and 2 employees).

To get an idea of our products -> the first one is a planning software for healthcare organizations (eg. HelpWing, firebrigade, pharmacy), the second one is a booking software for sport clubs and the third one is a competition software for sports hunting. You see very diverse. Include or ignore this info of our products as you like.

The design has to be a bootstrap 4 (or higher) design. We have licenced FontAwesome as iconset. Responsive design should come without saying.

• Starting page, product pages, news section, contact, team, services

```html
<!DOCTYPE html>
<html lang="en">
<head>
<meta charset="utf-8">
<title>velmor — We build your software</title>
<link href="https://fonts.googleapis.com/css2?family=Montserrat:wght@400;500;600;700;800&display=swap" rel="stylesheet">
<style>
:root{
  --orange:#f58131;
  --ink:#2b2f36;
  --text:#6f7379;
  --muted:#9a9da2;
  --band:#f3f4f4;
  --card:#e6e6e8;
  --white:#ffffff;
}
*{box-sizing:border-box;margin:0;padding:0}
html,body{width:1200px;height:3766px;overflow:hidden}
body{position:relative;background:var(--white);font-family:'Montserrat',sans-serif;color:var(--ink)}
.abs{position:absolute}
.brand{font-weight:700;color:var(--ink);letter-spacing:1px;display:flex;align-items:center;gap:8px}
.brand .dot{width:14px;height:14px;background:var(--orange)}
.nav{left:576px;top:33px;display:flex;gap:30px;font-size:12px;font-weight:500;letter-spacing:.4px}
.btn{background:var(--orange);color:var(--ink);font-size:11px;font-weight:600;letter-spacing:.5px;display:flex;align-items:center;justify-content:center}
.btn-corner{position:relative}
.btn-corner::after{content:"";position:absolute;right:3px;bottom:3px;border-left:9px solid transparent;border-bottom:9px solid var(--ink)}
.hero-bg{left:0;top:0;width:1200px;height:608px;background:radial-gradient(ellipse at 70% 30%,#f0f1f1 0%,#fafafa 45%,#ffffff 80%)}
.hero-title{left:0;width:1200px;top:170px;text-align:center;font-weight:800;font-size:72px;line-height:82px;letter-spacing:2px}
.hero-sub{left:0;width:1200px;top:346px;text-align:center;font-size:16px;line-height:27px;color:var(--text)}
.feature-band{left:0;top:608px;width:1200px;height:218px;background:var(--orange)}
.feature{position:absolute;top:40px;width:240px;color:#fff}
.feature h3{font-size:15px;font-weight:600;margin-top:20px}
.feature p{font-size:11px;line-height:22px;color:#fde0c9;margin-top:6px}
.section-title{font-weight:600;font-size:29px;letter-spacing:.5px}
.divider{display:flex;align-items:center;gap:14px}
.divider span{display:block;width:62px;height:1px;background:var(--orange)}
.divider i{display:block;border-left:8px solid var(--ink);border-top:5px solid transparent;border-bottom:5px solid transparent}
.photo{background:linear-gradient(135deg,#c9b8a6 0%,#6a7380 50%,#2e3640 100%)}
.about-text{left:592px;top:993px;width:445px;font-size:14px;line-height:22.4px;color:var(--text)}
.about-text p+p{margin-top:12px}
.link{font-size:12px;font-weight:600;letter-spacing:1.5px;color:var(--orange)}
.services-band{left:0;top:1370px;width:1200px;height:549px;background:var(--band)}
.service{position:absolute;top:147px;width:251px;height:325px;background:var(--card);padding:20px 23px}
.service h4{font-size:17px;font-weight:500;line-height:25px;margin-top:20px}
.service p{font-size:13.5px;line-height:22.5px;color:var(--muted);margin-top:12px}
.service .more{position:absolute;left:23px;top:268px;font-size:11.5px;font-weight:600;letter-spacing:1px;padding-bottom:8px;border-bottom:2px solid var(--orange)}
.center-title{left:0;width:1200px;text-align:center}
.center-div{left:0;width:1200px;display:flex;justify-content:center}
.tech{position:absolute;top:2097px;width:171px;height:155px;display:flex;align-items:center;justify-content:center;font-weight:700;font-size:26px;color:#4a4d52}
.tech.active{background:#fff;box-shadow:0 4px 18px rgba(0,0,0,.08);color:#3aa776}
.tech .sq{width:14px;height:14px;background:currentColor;margin-right:8px}
.vsep{position:absolute;top:2105px;width:1px;height:140px;background:#e9e9ea}
.member{position:absolute;top:2422px;width:200px;text-align:center}
.member h5{font-size:15px;font-weight:500;margin-top:14px}
.member small{display:block;font-size:9.5px;color:var(--text);margin-top:8px}
.news-band{left:0;top:2707px;width:1200px;height:700px;background:var(--band)}
.post{position:absolute;top:2853px;width:330px;height:363px;background:#fff;padding:15px 16px}
.post .img{width:299px;height:228px}
.meta{display:flex;align-items:center;gap:10px;margin-top:12px;font-size:10.5px;color:var(--muted)}
.tag{background:#fdeadd;color:var(--orange);padding:3px 8px}
.post h6{font-size:15.5px;font-weight:500;line-height:23.5px;margin-top:14px}
.cta-text{color:#fff}
.footer-links{font-size:11.5px;color:var(--text);line-height:26px}
.socials{top:3723px;left:760px;font-size:10px;font-weight:600;display:flex}
</style>
</head>
<body>

<!-- Header -->
<div class="hero-bg abs"></div>
<div class="brand abs" style="left:118px;top:22px;font-size:34px"><span class="dot"></span>VELMOR</div>
<nav class="nav abs"><span>HOME</span><span>PRODUCT</span><span>SERVICES</span><span>NEWS</span><span>TEAM</span></nav>
<div class="btn btn-corner abs" style="left:954px;top:25px;width:128px;height:33px">LET'S TALK</div>

<!-- Hero -->
<h1 class="hero-title abs">WE BUILD YOUR<br>SOFTWARE.</h1>
<p class="hero-sub abs">We are developing several products (currently 3 standard-software<br>products) which are all in different sectors</p>
<svg class="abs" style="left:592px;top:492px" width="16" height="102" viewBox="0 0 16 102">
  <line x1="8" y1="0" x2="8" y2="96" stroke="#555" stroke-width="1"/>
  <polyline points="2,84 8,92 14,84" fill="none" stroke="#555"/>
  <polyline points="2,90 8,98 14,90" fill="none" stroke="#555"/>
</svg>

<!-- Product band -->
<section class="feature-band abs">
  <div class="feature" style="left:162px">
    <svg width="30" height="30" viewBox="0 0 30 30" fill="none" stroke="#fff" stroke-width="2"><circle cx="15" cy="15" r="3" fill="#fff"/><path d="M15 2v6M15 22v6M2 15h6M22 15h6M6 6l4 4M20 20l4 4M24 6l-4 4M6 24l4-4"/></svg>
    <h3>Planning Software</h3>
    <p>Lorem ipsum dolor sit amet, consectetuer adipiscing elit, sed diam nonummy nibh euismod</p>
  </div>
  <div class="feature" style="left:495px">
    <svg width="32" height="32" viewBox="0 0 32 32" fill="none" stroke="#fff" stroke-width="2"><circle cx="16" cy="16" r="13"/><circle cx="16" cy="16" r="3" fill="#fff"/><path d="M6 6l5 5"/></svg>
    <h3>Booking Software</h3>
    <p>Lorem ipsum dolor sit amet, consectetuer adipiscing elit, sed diam nonummy nibh euismod</p>
  </div>
  <div class="feature" style="left:820px">
    <svg width="40" height="32" viewBox="0 0 40 32" fill="none" stroke="#fff" stroke-width="2"><circle cx="16" cy="16" r="13"/><circle cx="22" cy="16" r="13"/><circle cx="19" cy="16" r="3" fill="#fff"/></svg>
    <h3>Competition Software</h3>
    <p>Lorem ipsum dolor sit amet, consectetuer adipiscing elit, sed diam nonummy nibh euismod</p>
  </div>
</section>

<!-- About -->
<div class="photo abs" role="img" aria-label="Photo of the team working together at a computer" style="left:161px;top:899px;width:365px;height:392px"></div>
<svg class="abs" style="left:482px;top:1231px" width="55" height="60" viewBox="0 0 55 60"><polygon points="55,0 55,60 0,60" fill="#f58131"/></svg>
<h2 class="section-title abs" style="left:592px;top:907px">ABOUT VELMOR</h2>
<div class="divider abs" style="left:592px;top:955px"><span></span><i></i><span></span></div>
<div class="about-text abs">
  <p>Lorem ipsum dolor sit amet, consectetuer adipiscing elit, sed diam nonummy nibh euismod tincidunt ut laoreet dolore magna aliquam erat volutpat. Ut wisi enim ad minim veniam, quis nostrud exerci tation ullamcorper suscipit lobortis nisl ut aliquip ex ea commodo consequat.</p>
  <p>Duis autem vel eum iriure dolor in hendrerit in vulputate velit esse molestie consequat, vel illum dolore eu feugiat nulla facilisis at vero eros et accumsan et iusto odio dignissim qui blandit praesent luptatum zzril delenit augue duis dolore te feugait nulla facilisi.</p>
</div>
<div class="link abs" style="left:592px;top:1253px">LEARN MORE ABOUT US &nbsp;›</div>

<!-- Services -->
<section class="services-band abs">
  <h2 class="section-title abs" style="left:164px;top:66px">OUR SERVICES</h2>
  <div class="divider abs" style="left:162px;top:117px"><span></span><i></i><span></span></div>
  <svg class="abs" style="left:995px;top:78px" width="46" height="12" viewBox="0 0 46 12" fill="none" stroke-width="1.4"><path d="M12 6H1M5 2L1 6l4 4" stroke="#2b2f36"/><path d="M18 6h27M41 2l4 4-4 4" stroke="#f58131"/></svg>

  <div class="service" style="left:161px">
    <svg width="46" height="46" viewBox="0 0 46 46"><circle cx="23" cy="23" r="20" fill="#f58131"/><circle cx="23" cy="23" r="12" fill="#fbc79c"/><circle cx="23" cy="23" r="4" fill="#2b2f36"/></svg>
    <h4>Software consulting</h4>
    <p>Lorem ipsum dolor sit amet, consectetuer adipiscing elit, sed diam nonummy.</p>
    <span class="more">LEARN MORE</span>
  </div>
  <div class="service" style="left:438px">
    <svg width="46" height="46" viewBox="0 0 46 46"><rect x="4" y="4" width="14" height="14" fill="#f58131"/><circle cx="22" cy="24" r="16" fill="#2b2f36"/><circle cx="22" cy="24" r="9" fill="#fbc79c"/><circle cx="22" cy="24" r="4" fill="#f58131"/></svg>
    <h4>Legacy software modernization</h4>
    <p>Lorem ipsum dolor sit amet, consectetuer adipiscing elit, sed diam nonummy.</p>
    <span class="more">LEARN MORE</span>
  </div>
  <div class="service" style="left:716px">
    <svg width="46" height="46" viewBox="0 0 46 46"><circle cx="23" cy="25" r="19" fill="#2b2f36"/><circle cx="23" cy="25" r="12" fill="#f58131"/><circle cx="23" cy="25" r="5" fill="#fbc79c"/></svg>
    <h4>Software development outsourcing</h4>
    <p>Lorem ipsum dolor sit amet, consectetuer adipiscing elit, sed diam nonummy.</p>
    <span class="more">LEARN MORE</span>
  </div>
  <div class="service" style="left:995px">
    <svg width="46" height="46" viewBox="0 0 46 46" fill="none" stroke-width="3"><path d="M6 6l10 10-10 10M20 6l10 10-10 10" stroke="#2b2f36"/><path d="M20 20l10 10-10 10M34 20l8 10-8 10" stroke="#f58131"/></svg>
    <h4>Legacy software modernization</h4>
    <p>Lorem ipsum dolor sit amet, consectetuer adipiscing elit, sed diam nonummy.</p>
    <span class="more">LEARN MORE</span>
  </div>
</section>

<!-- Technology stack -->
<h2 class="section-title center-title abs" style="top:1997px">TECHNOLOGY STACK</h2>
<div class="center-div abs" style="top:2047px"><div class="divider"><span></span><i></i><span></span></div></div>
<div class="tech" style="left:180px">Nexa</div>
<div class="tech active" style="left:342px"><span class="sq"></span>Verdo</div>
<div class="tech" style="left:507px;color:#8a8d92"><span class="sq"></span>Jiva</div>
<div class="vsep" style="left:668px"></div>
<div class="tech" style="left:663px;color:#5a5d62"><span class="sq"></span>Tesso</div>
<div class="vsep" style="left:829px"></div>
<div class="tech" style="left:818px;color:#6d7076"><span class="sq"></span>Pylon</div>

<!-- Team -->
<h2 class="section-title center-title abs" style="top:2327px">MEET THE TEAM</h2>
<div class="center-div abs" style="top:2376px"><div class="divider"><span></span><i></i><span></span></div></div>
<svg width="0" height="0" class="abs"><defs>
  <linearGradient id="hexGrad" x1="0" y1="0" x2="0" y2="1"><stop offset="0" stop-color="#d7d7da"/><stop offset="1" stop-color="#8c8f95"/></linearGradient>
</defs></svg>
<div class="member" style="left:200px">
  <svg role="img" aria-label="Portrait of Consectetuer" width="153" height="178" viewBox="0 0 153 178"><polygon points="76.5,0 153,44.5 153,133.5 76.5,178 0,133.5 0,44.5" fill="url(#hexGrad)"/></svg>
  <h5>Consectetuer</h5><small>CEO / Founder</small>
</div>
<div class="member" style="left:400px">
  <svg role="img" aria-label="Portrait of Commodo" width="153" height="178" viewBox="0 0 153 178"><polygon points="76.5,0 153,44.5 153,133.5 76.5,178 0,133.5 0,44.5" fill="#6f6a6a"/></svg>
  <h5>Commodo</h5><small>COO / Co-Founder</small>
</div>
<div class="member" style="left:600px">
  <svg role="img" aria-label="Portrait of Suscipit Lobortis" width="153" height="178" viewBox="0 0 153 178"><polygon points="76.5,0 153,44.5 153,133.5 76.5,178 0,133.5 0,44.5" fill="#e3d6cf"/></svg>
  <h5>Suscipit Lobortis</h5><small>Product Design</small>
</div>
<div class="member" style="left:800px">
  <svg role="img" aria-label="Portrait of Autem Vel" width="153" height="178" viewBox="0 0 153 178"><polygon points="76.5,0 153,44.5 153,133.5 76.5,178 0,133.5 0,44.5" fill="url(#hexGrad)"/></svg>
  <h5>Autem Vel</h5><small>Special Advisor</small>
</div>

<!-- News -->
<section class="news-band abs"></section>
<h2 class="section-title center-title abs" style="top:2765px">WHAT’S NEW</h2>
<div class="center-div abs" style="top:2814px"><div class="divider"><span></span><i></i><span></span></div></div>
<article class="post" style="left:256px">
  <div class="img" role="img" aria-label="Photo of colleagues in a modern tech office" style="background:linear-gradient(135deg,#2c4a6e,#6d8fb0 50%,#1d2f47)"></div>
  <div class="meta"><span class="tag">Blog</span><span>▢ April 20, 2022</span></div>
  <h6>Lorem ipsum dolor sit amet, consectetuer adipiscing elit, sed diam nonummy nibh euismod.</h6>
</article>
<article class="post" style="left:617px">
  <div class="img" role="img" aria-label="Photo of a cup of coffee surrounded by coffee beans" style="background:radial-gradient(circle at 60% 55%,#f2efe9 0%,#9a7a5e 22%,#3c2a20 55%,#1b1715 100%)"></div>
  <div class="meta"><span class="tag">Press Release</span><span>▢ April 20, 2022</span></div>
  <h6>Lorem ipsum dolor sit amet, consectetuer adipiscing elit.</h6>
</article>

<!-- Call to action -->
<svg class="abs" style="left:161px;top:3286px" width="870" height="214" viewBox="0 0 870 214">
  <polygon points="0,0 796,0 862,214 0,214" fill="#f58131"/>
</svg>
<div class="cta-text abs" style="left:199px;top:3341px;font-size:28px;font-weight:600;letter-spacing:.5px">WANT TO WORK WITH US?</div>
<div class="cta-text abs" style="left:199px;top:3389px;font-size:22px;line-height:34px">Follow Your Vision Software<br>Development Services</div>
<div class="btn btn-corner abs" style="left:808px;top:3379px;width:127px;height:34px;background:#fff">LET'S TALK</div>

<!-- Footer -->
<div class="brand abs" style="left:161px;top:3566px;font-size:34px"><span class="dot"></span>VELMOR</div>
<div class="footer-links abs" style="left:387px;top:3564px">Home<br>About<br>Services</div>
<div class="footer-links abs" style="left:484px;top:3564px">Products<br>Team<br>Contact</div>
<div class="abs" style="left:637px;top:3570px;font-size:10.5px;font-weight:500;line-height:21px;color:var(--ink)">Address Lorem ipsum<br>418 Maple Row<br>Brookfield, AB 90210</div>
<div class="abs" style="left:760px;top:3580px;width:56px;height:1px;background:#e1e1e2"></div>
<div class="abs" style="left:842px;top:3567px;font-size:29px;font-weight:500;color:var(--orange)">123.555.0190</div>
<div class="abs" style="left:842px;top:3609px;font-size:16px;color:var(--text)">info@velmor.com</div>
<div class="abs" style="left:0;top:3700px;width:1200px;height:1px;background:#ececec"></div>
<div class="abs" style="left:161px;top:3723px;font-size:10px;color:var(--text)">© 2022 Velmor. All right reserved.</div>
<div class="socials abs"><span style="width:104px">Facenet.</span><span style="width:54px">Linkly.</span><span style="width:82px">Instaframe.</span><span>Chirper.</span></div>

</body>
</html>
```